Design our beautiful and attractive PowerPoint template presentation

As you can see in the files attached below within this brief, we would like pls to receive a proposal for our Ravlo Drive Systems a powerpoint template which would include:
- open slide
- agenda slide
- 5 different main chapter slides , for examples below but chapter name shall be replaced according to need:
* about us
* products
* applications
* technical specifications
* testing and benchmark
- Q&A slide
- Conclusion slide
- Closing side
Pls also take a look to the web site being developed (under construction) to ensure you keep the same look and feel: http://rvdsx.pelmaro.example/index.php?id=308

Target Market(s)

Industry, multi channels

Industry/Entity Type

B-t-B mechanical parts distributors

Font styles to use
Other font styles liked:
• Pls see the font provided into the brief attached files

Requirements
Must have
• Follow the color, font and logo provided into the brief attached files
Nice to have
• Animated slides

```html
<!DOCTYPE html>
<html lang="en">
<head>
<meta charset="utf-8">
<title>Ravlo Drive Systems – Presentation Template</title>
<link rel="stylesheet" href="https://fonts.googleapis.com/css2?family=Fira+Sans:wght@300;400;500;600;700&family=Open+Sans:ital,wght@0,400;0,600;1,400&display=swap">
<style>
  :root{
    --navy:#0a5fb4;
    --blue:#0c6fc4;
    --sky:#3a9fdc;
    --pale:#9ed6f2;
    --row:#d5e6f7;
    --grey:#b4b9bf;
    --photo:#8d96a0;
    --placeholder:#616161;
    --ink:#262626;
    --stage:#d6d6d6;
  }
  *{box-sizing:border-box;margin:0;padding:0}
  html,body{width:1200px;height:1200px;overflow:hidden}
  body{background:var(--stage);font-family:"Open Sans",sans-serif;color:var(--ink);position:relative}

  .slide{position:absolute;width:369px;height:208px;background:#fff;overflow:hidden;box-shadow:0 6px 9px rgba(0,0,0,.28)}
  .c1{left:27px}.c2{left:414px}.c3{left:800px}
  .r1{top:124px}.r2{top:362px}.r3{top:600px}.r4{top:838px}

  .tab{position:absolute;left:100px;top:0;width:169px;height:6px;background:var(--navy);clip-path:polygon(0 0,100% 0,97% 100%,3% 100%)}
  .foot-line{position:absolute;left:0;bottom:2px;width:100%;height:3px;background:var(--blue)}
  .page-no{position:absolute;right:0;bottom:5px;width:44px;height:10px;background:var(--grey);clip-path:polygon(22% 0,100% 0,100% 100%,0 100%);color:#fff;font:500 5px/10px "Fira Sans",sans-serif;text-align:center;padding-left:8px}

  .head{position:absolute;top:13px;left:0;width:100%;text-align:center}
  .head h2{font:600 10.5px/1.2 "Fira Sans",sans-serif;color:var(--blue);text-transform:uppercase}
  .head p{font:400 7.6px/1.2 "Fira Sans",sans-serif;color:var(--ink)}
  .dots{display:flex;gap:1.5px;justify-content:center;margin-top:6px}
  .dots i{display:block;width:5px;height:5px;border-radius:50%}
  .dots i:nth-child(1){background:var(--navy)}
  .dots i:nth-child(2){background:var(--blue)}
  .dots i:nth-child(3){background:var(--sky)}
  .dots i:nth-child(4){background:var(--pale)}

  .txt{position:absolute;font-size:5.2px;line-height:9.2px;overflow:hidden}
  .txt em{display:block;font-style:italic;color:var(--navy);font-size:6px}
  .txt em.light{color:var(--sky)}
  .photo{position:absolute;background:linear-gradient(160deg,#c9cfd5,var(--photo) 60%,#5c6670)}

  /* cover */
  .cover-band{position:absolute;inset:0}
  .brand{position:absolute;font-family:"Fira Sans",sans-serif;color:#fff}
  .brand b{display:block;font-weight:700;font-size:21px;line-height:1;letter-spacing:.5px}
  .brand span{display:block;font-weight:700;font-size:5.6px;letter-spacing:.5px;margin-top:2px}
  .cover-title{position:absolute;right:20px;top:122px;text-align:right;font:400 17.5px/23px "Fira Sans",sans-serif;color:var(--blue);text-transform:uppercase}
  .cover-sub{position:absolute;right:20px;top:172px;font:300 7px "Fira Sans",sans-serif;color:#9aa0a6;text-transform:uppercase}

  /* agenda */
  .agenda-title{position:absolute;right:263px;top:90px;text-align:right;font:600 10.5px/14.5px "Fira Sans",sans-serif;color:var(--blue);text-transform:uppercase}
  .agenda-title .dots{justify-content:flex-end;margin-top:4px}
  .agenda-rule{position:absolute;left:114px;top:26px;width:1px;height:154px;background:var(--blue)}
  .agenda-item{position:absolute;left:128px;width:230px;height:40px}
  .agenda-num{position:absolute;left:0;top:0;width:19px;height:19px;border-radius:50%;background:var(--grey);color:var(--blue);font:600 12px/19px "Fira Sans",sans-serif;text-align:center}
  .agenda-item h3{position:absolute;left:29px;top:-1px;font:500 6.4px/1.2 "Fira Sans",sans-serif;color:var(--blue)}
  .agenda-item p{position:absolute;left:29px;top:7px;width:190px;font-size:4.8px;line-height:7.6px}

  /* table */
  .data-table{position:absolute;left:17px;top:81px;width:332px;border-collapse:collapse}
  .data-table th{background:var(--sky);height:14px;border:1px solid var(--sky)}
  .data-table td{height:13.8px;border:1px solid var(--sky)}
  .data-table tr:nth-child(odd) td{background:var(--row)}
  .data-table .w1{width:108px}.data-table .w2{width:112px}

  .image-box{position:absolute;left:17px;top:57px;width:166px;height:117px;background:var(--placeholder);color:#fff;font:400 17px/117px "Open Sans",sans-serif;text-align:center}

  /* steps */
  .steps-band{position:absolute;left:0;top:70px;width:100%;height:26px;background:var(--grey)}
  .step{position:absolute;top:77px;width:96px;text-align:center}
  .step-num{width:28px;height:28px;margin:0 auto;border-radius:50%;background:var(--blue);border:2px solid #fff;box-shadow:0 0 0 1px var(--blue);color:#fff;font:600 11px/24px "Fira Sans",sans-serif}
  .step h4{margin-top:9px;font:500 5.2px "Fira Sans",sans-serif;color:var(--sky)}
  .step p{margin-top:4px;font-size:4.6px;line-height:7.2px;text-align:left}

  /* closing */
  .contact{position:absolute;left:106px;top:168px;color:#fff;font-size:4.4px;line-height:6.6px;border-left:1px solid #fff;padding-left:5px}
</style>
</head>
<body>

<!-- Cover -->
<section class="slide c1 r1">
  <svg class="cover-band" width="369" height="208" viewBox="0 0 369 208">
    <polygon points="0,131 369,54 369,62 0,145" fill="#b4b9bf"/>
    <polygon points="0,0 369,0 369,54 0,131" fill="#0c6fc4"/>
  </svg>
  <div class="brand" style="left:22px;top:19px"><b>RAVLO</b><span style="color:#bfe3f8">DRIVE SYSTEMS</span></div>
  <h1 class="cover-title">Your headline text<br>here to put</h1>
  <p class="cover-sub">Lorem ipsum is simply dummy has been</p>
</section>

<!-- Agenda -->
<section class="slide c2 r1">
  <div class="tab"></div>
  <div class="agenda-title">Your<br>headline<br>here<div class="dots"><i></i><i></i><i></i><i></i></div></div>
  <div class="agenda-rule"></div>
  <div class="agenda-item" style="top:28px"><div class="agenda-num">1</div><h3>Ledgrix builds automation in stages</h3><p>System to reach full automation thanks to the Ledgrix AI. Ledgrix AI automates allows users to communicate seamlessly with it, viewing it as a trusted advisor over time for all their accounting queries.</p></div>
  <div class="agenda-item" style="top:70px"><div class="agenda-num">2</div><h3>Ledgrix builds automation in stages</h3><p>System to reach full automation thanks to the Ledgrix AI. Ledgrix AI automates allows users to communicate seamlessly with it, viewing it as a trusted advisor over time for all their accounting queries.</p></div>
  <div class="agenda-item" style="top:113px"><div class="agenda-num">3</div><h3>Ledgrix builds automation in stages</h3><p>System to reach full automation thanks to the Ledgrix AI. Ledgrix AI automates allows users to communicate seamlessly with it, viewing it as a trusted advisor over time for all their accounting queries.</p></div>
  <div class="agenda-item" style="top:158px"><div class="agenda-num">4</div><h3>Ledgrix builds automation in stages</h3><p>System to reach full automation thanks to the Ledgrix AI. Ledgrix AI automates allows users to communicate seamlessly with it, viewing it as a trusted advisor over time for all their accounting queries.</p></div>
  <div class="foot-line"></div><div class="page-no">12</div>
</section>

<!-- Two column text -->
<section class="slide c3 r1">
  <div class="tab"></div>
  <div class="head"><h2>Your headline here</h2><p>Lorem ipsum is simply dummy has been</p><div class="dots"><i></i><i></i><i></i><i></i></div></div>
  <p class="txt" style="left:17px;top:57px;width:164px;height:126px">AI automated accounting<br>Ledgrix builds automation in stages on top of its current system to reach full automation thanks to the Ledgrix AI. Ledgrix AI automates every manual task performed by the user. It starts by connecting to all sources of accounting data such as bank accounts, credit card, webshop or document management systems (Filebay or Vaultr). Based on these datas, Ledgrix AI creates bookings and generates financial reports. Finally, Ledgrix AI features chat-like interface that allows users to communicate seamlessly with it, viewing it as a trusted advisor over time for all their accounting queries. software licenses easier for software developers. It also makes the management and resale of software license easier for software owners. All in all, TaaL has a higher</p>
  <div style="position:absolute;left:183px;top:58px;width:1px;height:116px;background:var(--blue)"></div>
  <p class="txt" style="left:190px;top:57px;width:166px;height:126px">value as a normal . normal software license.<em>Blockchain software license or Token-as-a-License</em>It is possible to create tokens on blockchain that represent software licenses, also known as Token-as-a-Licence (TaaL). Ledgrix creates TaaL by using the Corvane official wallet which interacts with the Corvane blockchain. Upon purchase of TaaL, the token holder is free to transfer or sell TaaL using secondary market that is built directly over the blockchain, in our case, the Corvane marketplace. Ledgrix checks the validity of a token against the blockchain ensuring that token holders have access to the software. TaaL make distribution and securisation of software licenses easier for software developers. It also makes the management and resale of software license easier for software</p>
  <div class="foot-line"></div><div class="page-no">12</div>
</section>

<!-- Table -->
<section class="slide c1 r2">
  <div class="tab"></div>
  <div class="head"><h2>Your headline here</h2><p>Lorem ipsum is simply dummy has been</p><div class="dots"><i></i><i></i><i></i><i></i></div></div>
  <p class="txt" style="left:17px;top:57px;width:340px;height:16px;font-size:4.8px;line-height:7.2px">Ledgrix builds automation in stages on top of its current system to reach full automation thanks to the Ledgrix AI. Ledgrix AI automates every manual task performed by the user. It starts by connecting to all sources of accounting data such as bank accounts, credit card, webshop</p>
  <table class="data-table">
    <tr><th class="w1"></th><th class="w2"></th><th></th></tr>
    <tr><td></td><td></td><td></td></tr>
    <tr><td></td><td></td><td></td></tr>
    <tr><td></td><td></td><td></td></tr>
    <tr><td></td><td></td><td></td></tr>
    <tr><td></td><td></td><td></td></tr>
    <tr><td></td><td></td><td></td></tr>
  </table>
  <div class="foot-line"></div><div class="page-no">12</div>
</section>

<!-- Image + text -->
<section class="slide c2 r2">
  <div class="tab"></div>
  <div class="head"><h2>Your headline here</h2><p>Lorem ipsum is simply dummy has been</p><div class="dots"><i></i><i></i><i></i><i></i></div></div>
  <div class="image-box">Image</div>
  <p class="txt" style="left:191px;top:57px;width:170px;height:122px">value as a normal . normal software license.<em>Blockchain software license or Token-as-a-License</em>It is possible to create tokens on blockchain that represent software licenses, also known as Token-as-a-Licence (TaaL). Ledgrix creates TaaL by using the Corvane official wallet which interacts with the Corvane blockchain. Upon purchase of TaaL, the token holder is free to transfer or sell TaaL using secondary market that is built directly over the blockchain, in our case, the Corvane marketplace. Ledgrix checks the validity of a token against the blockchain ensuring that token holders have access to the software. TaaL make distribution and securisation of software licenses easier for software developers. It also makes the management and resale of software license easier for software</p>
  <div class="foot-line"></div><div class="page-no">12</div>
</section>

<!-- Full text -->
<section class="slide c3 r2">
  <div class="tab"></div>
  <div class="head"><h2>Your headline here</h2><p>Lorem ipsum is simply dummy has been</p><div class="dots"><i></i><i></i><i></i><i></i></div></div>
  <p class="txt" style="left:15px;top:50px;width:342px;height:60px"><em class="light">AI automated accounting</em>Ledgrix builds automation in stages on top of its current system to reach full automation thanks to the Ledgrix AI. Ledgrix AI automates every manual task performed by the user. It starts by connecting to all sources of accounting data such as bank accounts, credit card, webshop or document management systems (Filebay or Vaultr). Based on these datas, Ledgrix AI creates bookings and generates financial reports. Finally, Ledgrix AI features chat-like interface that allows users to communicate seamlessly with it, viewing it as a trusted advisor over time for all their accounting queries.</p>
  <p class="txt" style="left:15px;top:114px;width:342px;height:70px"><em class="light">Blockchain software license or Token-as-a-License (TaaL)</em>It is possible to create tokens on blockchain that represent software licenses, also known as Token-as-a-Licence (TaaL). Ledgrix creates TaaL by using the Corvane official wallet which interacts with the Corvane blockchain. Upon purchase of TaaL, the token holder is free to transfer or sell TaaL using secondary market that is built directly over the blockchain, in our case, the Corvane marketplace. Ledgrix checks the validity of a token against the blockchain ensuring that token holders have access to the software. TaaL make distribution and securisation of software licenses easier for software developers. It also makes the management and resale of software license easier for software owners. All in all, TaaL has a higher value as a normal software license.</p>
  <div class="foot-line"></div><div class="page-no">12</div>
</section>

<!-- Chart -->
<section class="slide c1 r3">
  <div class="tab"></div>
  <div class="head"><h2>Your headline here</h2><p>Lorem ipsum is simply dummy has been</p><div class="dots"><i></i><i></i><i></i><i></i></div></div>
  <svg style="position:absolute;left:23px;top:45px" width="194" height="122" viewBox="0 0 194 122" font-family="Open Sans, sans-serif" font-size="3.8" fill="#333" text-anchor="middle">
    <g fill="#4a90d2" stroke="#8cc2ec" stroke-width=".4">
      <rect x="0" y="34.5" width="15.4" height="75.5"/>
      <rect x="16" y="18.2" width="15.4" height="91.8"/>
      <rect x="32" y="49.6" width="15.4" height="60.4"/>
      <rect x="48" y="76.7" width="15.4" height="33.3"/>
      <rect x="64" y="103.1" width="15.4" height="6.9"/>
      <rect x="80" y="90.9" width="15.4" height="19.1"/>
      <rect x="96" y="96.9" width="15.4" height="13.1"/>
      <rect x="112" y="81.1" width="15.4" height="28.9"/>
      <rect x="128" y="75.4" width="15.4" height="34.6"/>
      <rect x="144" y="41.4" width="15.4" height="68.6"/>
      <rect x="160" y="28.9" width="15.4" height="81.1"/>
      <rect x="176" y="10" width="15.4" height="100"/>
    </g>
    <text x="7.7" y="32.5">120</text><text x="23.7" y="16.2">146</text><text x="39.7" y="47.6">96</text>
    <text x="55.7" y="74.7">53</text><text x="71.7" y="101.1">11</text><text x="87.7" y="88.9">30.3</text>
    <text x="103.7" y="94.9">20.9</text><text x="119.7" y="79.1">46</text><text x="135.7" y="73.4">55</text>
    <text x="151.7" y="39.4">109</text><text x="167.7" y="26.9">129</text><text x="183.7" y="8">159</text>
    <text x="7.7" y="117">Jan…</text><text x="23.7" y="117">Febr…</text><text x="39.7" y="117">March</text>
    <text x="55.7" y="117">April</text><text x="71.7" y="117">May</text><text x="87.7" y="117">Jun</text>
    <text x="103.7" y="117">July</text><text x="119.7" y="117">Aug…</text><text x="135.7" y="117">Sep…</text>
    <text x="151.7" y="117">Oct…</text><text x="167.7" y="117">Nov…</text><text x="183.7" y="117">Dec…</text>
  </svg>
  <p class="txt" style="left:232px;top:48px;width:120px;height:120px;font-size:4.6px;line-height:7.1px">Ledgrix builds automation in stages on top of its current system to reach full automation thanks to the Ledgrix AI. Ledgrix AI automates every manual task performed by the user. It starts by connecting to all sources of accounting data such as bank accounts, credit card, webshop or document management systems (Filebay or Vaultr). Based on these datas, Ledgrix AI creates bookings and generates financial reports. Finally, Ledgrix AI features chat-like interface that allows users to communicate seamlessly with it, viewing it as a trusted advisor over time for all their accounting queries.<em style="font-size:5px;margin-top:4px">Blockchain software license or Token-as-a-License (TaaL)</em><b style="font-weight:600">It is possible to create tokens on blockchain that</b></p>
  <div class="foot-line"></div><div class="page-no">12</div>
</section>

<!-- Steps -->
<section class="slide c2 r3">
  <div class="tab"></div>
  <div class="head"><h2>Your headline here</h2><p>Lorem ipsum is simply dummy has been</p><div class="dots"><i></i><i></i><i></i><i></i></div></div>
  <p class="txt" style="left:20px;top:53px;width:330px;height:15px;font-size:4.6px;line-height:7px;text-align:center">Ledgrix builds automation in stages on top of its current system to reach full automation thanks to the Ledgrix AI. Ledgrix AI automates every manual task performed by the user. It starts by connecting to all sources of accounting data such as bank accounts, credit card, webshop</p>
  <div class="steps-band"></div>
  <div class="step" style="left:18px"><div class="step-num">1</div><h4>Ledgrix builds</h4><p>Ledgrix builds automation in stages on top of its current system to reach full automation thanks to the Ledgrix AI. Ledgrix AI automates every manual task performed by the user. It starts by connecting to all sources of accounting</p></div>
  <div class="step" style="left:137px"><div class="step-num">2</div><h4>Ledgrix builds</h4><p>Ledgrix builds automation in stages on top of its current system to reach full automation thanks to the Ledgrix AI. Ledgrix AI automates every manual task performed by the user. It starts by connecting to all sources of accounting</p></div>
  <div class="step" style="left:251px"><div class="step-num">3</div><h4>Ledgrix builds</h4><p>Ledgrix builds automation in stages on top of its current system to reach full automation thanks to the Ledgrix AI. Ledgrix AI automates every manual task performed by the user. It starts by connecting to all sources of accounting</p></div>
  <div class="foot-line"></div><div class="page-no">12</div>
</section>

<!-- Photo + text -->
<section class="slide c3 r3">
  <div class="tab"></div>
  <div class="head"><h2>Your headline here</h2><p>Lorem ipsum is simply dummy has been</p><div class="dots"><i></i><i></i><i></i><i></i></div></div>
  <div class="photo" role="img" aria-label="Photo of a businessman standing in a bright open-plan office" style="left:16px;top:58px;width:98px;height:112px"></div>
  <p class="txt" style="left:126px;top:59px;width:232px;height:124px">AI automated accounting<br>Ledgrix builds automation in stages on top of its current system to reach full automation thanks to the Ledgrix AI. Ledgrix AI automates every manual task performed by the user. It starts by connecting to all sources of accounting data such as bank accounts, credit card, webshop or document management systems (Filebay or Vaultr). Based on these datas, Ledgrix AI creates bookings and generates financial reports. Finally, Ledgrix AI features chat-like interface that allows users to communicate seamlessly with it, viewing it as a trusted advisor over time for all their accounting queries. software licenses easier for software developers. It also makes the management and resale of software license easier for software owners. All in all, TaaL has a higher value as a normal . normal software license.<em>Blockchain software license or Token-as-a-License</em>It is possible to create tokens on blockchain that represent software licenses, also known as Token-as-a-Licence (TaaL). Ledgrix creates TaaL by using the Corvane official wallet which</p>
  <div class="foot-line"></div><div class="page-no">12</div>
</section>

<!-- Two photos -->
<section class="slide c1 r4">
  <div class="tab"></div>
  <div class="head"><h2>Your headline here</h2><p>Lorem ipsum is simply dummy has been</p><div class="dots"><i></i><i></i><i></i><i></i></div></div>
  <div class="photo" role="img" aria-label="Photo of a business team walking through an office" style="left:16px;top:58px;width:75px;height:112px"></div>
  <p class="txt" style="left:99px;top:58px;width:84px;height:118px">AI automated accounting<br>Ledgrix builds automation in stages on top of its current system to reach full automation thanks to the Ledgrix AI. Ledgrix AI automates every manual task performed by the user. It starts by connecting to all sources of accounting data such as bank accounts, credit card, webshop or document management systems (Filebay or Vaultr). Based on these datas,</p>
  <div class="photo" role="img" aria-label="Photo of a business team walking through an office" style="left:188px;top:58px;width:75px;height:112px"></div>
  <p class="txt" style="left:271px;top:58px;width:84px;height:118px">AI automated accounting<br>Ledgrix builds automation in stages on top of its current system to reach full automation thanks to the Ledgrix AI. Ledgrix AI automates every manual task performed by the user. It starts by connecting to all sources of accounting data such as bank accounts, credit card, webshop or document management systems (Filebay or Vaultr). Based on these datas,</p>
  <div class="foot-line"></div><div class="page-no">12</div>
</section>

<!-- Wide photo + text -->
<section class="slide c2 r4">
  <div class="tab"></div>
  <div class="head"><h2>Your headline here</h2><p>Lorem ipsum is simply dummy has been</p><div class="dots"><i></i><i></i><i></i><i></i></div></div>
  <div class="photo" role="img" aria-label="Photo of colleagues walking together through a modern office" style="left:16px;top:59px;width:176px;height:111px"></div>
  <p class="txt" style="left:204px;top:58px;width:152px;height:118px">AI automated accounting<br>Ledgrix builds automation in stages on top of its current system to reach full automation thanks to the Ledgrix AI. Ledgrix AI automates every manual task performed by the user. It starts by connecting to all sources of accounting data such as bank accounts, credit card, webshop or document management systems (Filebay or Vaultr). Based on these datas, Ledgrix AI creates bookings and generates financial reports. Finally, Ledgrix AI features chat-like interface that allows users to communicate seamlessly with it, viewing it as a trusted advisor over time for all their accounting queries. software licenses easier for software developers. It also makes the management and resale of software license</p>
  <div class="foot-line"></div><div class="page-no">12</div>
</section>

<!-- Closing -->
<section class="slide c3 r4">
  <svg class="cover-band" width="369" height="208" viewBox="0 0 369 208">
    <polygon points="0,140 369,15 369,20 0,150" fill="#b4b9bf"/>
    <polygon points="0,150 369,20 369,208 0,208" fill="#0c6fc4"/>
  </svg>
  <div class="brand" style="left:16px;top:166px"><b style="font-size:18px">RAVLO</b><span style="font-size:5px;color:#bfe3f8">DRIVE SYSTEMS</span></div>
  <div class="contact">T: +000 000 0000<br>E: info@ravlo-drive.example<br>P.O. Box 0000, Harlow Street<br>Northgate 0000</div>
</section>

</body>
</html>
```